Expo Program Guide Design and Logo for Lantern Grove Shows

First, we are looking for a new logo for "Lantern Grove Shows" similar in feel to our other brands, Harborlight Market and Tall Cedar Expo. Attached is a graphic showing the three current logos.

Second we are looking for a new overall layout for our holistic living expo program guides that apply this new logo. Each 16-24 page guide has the following sections that need to have templates created that carry out the same look/feel.

a) front and back covers (similar in feel to the Denver Guide attached page 1 or Chicago page 1)
b) Welcome page (similar to the Chicago Guide attached page 3)
c) Expo lecture overview page (similar in feel to the Chicago Guide attached page 7, should only allow for 4 presentation rooms and be vertical to the page.)
d) Left detail page of presentations (similar in feel to the Chicago Guide attached page 34)
e) Right detail page of presentations (similar in feel to the Chicago Guide attached page 35)
f) Detail page for exhibitors (similar in feel to the Chicago Guide attached page 24)
g) Detail page for featured presenters (similar in feel to the Chicago Guide attached page 12)
f) Detail page for secondary featured presenters (similar in feel to the Chicago Guide attached page 15)

Target Market(s)

Casual female 25-54 with interest in holistic subjects

Requirements
Must have
• Logo should have horizontal aspect ratio.

Although samples may be in AI, PSD or PDF, we must have the templates in InDesign native files at the conclusion of the project for all pages of the guide.

Final logo should be vector based.

```html
<!DOCTYPE html>
<html lang="en">
<head>
<meta charset="utf-8">
<title>Lantern Grove Shows – Expo 2013 Program Guide</title>
<link href="https://fonts.googleapis.com/css2?family=Baloo+2:wght@600;700&family=Oswald:wght@400;500&family=Open+Sans:wght@400;600;700&display=swap" rel="stylesheet">
<style>
:root{
  --magenta:#a4237e;
  --plum:#8a2868;
  --lime:#a9cf38;
  --chartreuse:#cbdc2a;
  --orange:#ee5a24;
  --cyan:#22b3df;
  --yellow:#f3e11c;
  --grey-light:#e2e2e3;
  --grey-dark:#58585a;
  --ink:#6d6e71;
  --white:#ffffff;
  --display:'Baloo 2', 'Trebuchet MS', sans-serif;
  --condensed:'Oswald', 'Arial Narrow', sans-serif;
  --body:'Open Sans', Arial, sans-serif;
}
*{box-sizing:border-box;margin:0;padding:0}
html,body{width:1200px;height:539px;overflow:hidden;background:#fff}
.canvas{position:relative;width:1200px;height:539px;background:#fff;overflow:hidden;font-family:var(--body)}
.page{position:absolute;top:31px;width:376px;height:484px;background:#fff;overflow:hidden;box-shadow:2px 3px 6px rgba(0,0,0,.35)}
.page--cover{left:18px}
.page--welcome{left:408px}
.page--schedule{left:799px}
.page>svg.shapes{position:absolute;inset:0;width:100%;height:100%}
.abs{position:absolute}

/* cover */
.cover-photo{position:absolute;inset:0;background:linear-gradient(180deg,#6fa9dc 0%,#9cc7ea 42%,#5d93c2 60%,#3e7aa8 70%,#c9b7a0 86%,#b59c82 100%)}
.brand{font-family:var(--display);font-weight:700;color:var(--white);line-height:1;letter-spacing:.3px;white-space:nowrap}
.brand-dot{display:inline-block;width:.45em;height:.45em;border-radius:50%;background:var(--white);margin-right:.25em;vertical-align:.12em}
.cover .brand-name{left:26px;top:40px;font-size:25px}
.cover .brand-year{left:108px;top:70px;font-size:23px}
.event-info{left:236px;top:116px;color:var(--magenta);font-family:var(--display);font-weight:700;line-height:1.05}
.event-city{font-size:22px}
.event-venue{font-size:11.5px}
.event-dates{font-size:18px;margin-top:2px}
.event-hours,.event-admission{font-size:10.5px}
.cover-tagline{left:116px;top:226px;font-family:var(--condensed);font-weight:500;font-size:23px;line-height:1;text-transform:uppercase}
.cover-tagline .t1{color:var(--yellow)}
.cover-tagline .t2{color:var(--white)}
.cover-stats{left:136px;top:392px;font-family:var(--display);font-weight:700;color:var(--white);line-height:1.02}
.cover-stats .s1{font-size:19px}
.cover-stats .s2,.cover-stats .s3{font-size:14px}
.speaker{color:var(--white);font-family:var(--body)}
.speaker h3{font-family:var(--display);font-weight:700;font-size:11.5px;line-height:1;text-transform:uppercase}
.speaker ul{list-style:none;font-size:6.4px;line-height:1.35}
.speaker li::before{content:"■ ";font-size:5px;vertical-align:1px}
.speaker--keynote{left:12px;top:314px;width:90px}
.speaker--right{left:296px;top:371px;width:76px}
.speaker--bottom{left:30px;top:443px;width:140px}
.portrait{background:linear-gradient(160deg,#f1d2b8,#c99878 60%,#6b4a3a)}
.portrait--round{position:absolute;border-radius:50%;border:1.5px solid #fff}

/* welcome */
.section-bar{background:var(--orange);color:var(--white);font-family:var(--display);font-weight:600;height:15px;line-height:15px;padding-left:10px}
.toc-title{left:0;top:60px;width:119px;font-size:13px}
.toc{left:22px;top:84px;width:108px;list-style:none;font-size:6px;color:var(--ink);line-height:8.4px;text-transform:uppercase}
.toc li{display:flex;white-space:nowrap}
.toc li span:first-child{width:86px}
.welcome-title{left:228px;top:60px;font-family:var(--display);font-weight:700;color:var(--white);font-size:19px}
.welcome-greeting{left:166px;top:100px;font-weight:700;font-size:9px;color:var(--grey-dark)}
.welcome-copy{left:166px;top:114px;width:204px;font-size:5.9px;line-height:7.9px;color:#7b7c7f}
.welcome-sign{text-align:right;margin-top:5px}
.welcome .brand-name{left:24px;top:296px;font-size:13.5px}
.welcome .brand-year{left:50px;top:314px;font-size:14px}
.team-note{left:22px;top:352px;width:158px;color:var(--white);font-size:6px;line-height:7.5px}
.team-note strong{display:block;font-weight:600}
.expo-title{left:225px;top:322px;width:151px;font-size:11px}
.expo-copy{left:213px;top:344px;width:155px;font-size:5.9px;line-height:7.5px;color:#7b7c7f}
.expo-photo{left:226px;top:384px;width:62px;height:55px;background:linear-gradient(135deg,#5b6c7a,#a89a86 45%,#3f4b55)}
.expo-copy-side{left:294px;top:384px;width:74px;font-size:5.9px;line-height:7.5px;color:#7b7c7f}
.folio{position:absolute;right:12px;bottom:8px;display:flex;align-items:center;gap:3px;font-family:var(--display);font-weight:600;font-size:5.5px;color:var(--grey-dark);text-transform:uppercase}
.folio b{display:inline-block;width:13px;height:13px;border-radius:50% 50% 50% 0;background:var(--plum);color:#fff;font-size:6px;line-height:13px;text-align:center}

/* schedule */
.schedule-title{left:150px;top:10px;width:226px;height:28px;font-family:var(--display);font-weight:700;font-size:15px;color:var(--white);text-align:right;padding-right:16px;line-height:30px}
.feature-portrait{left:22px;top:24px;width:92px;height:92px}
.tag{display:block;height:9px;line-height:9.5px;font-family:var(--display);font-weight:600;font-size:7.4px;color:var(--white);padding-left:4px;margin-bottom:1px;white-space:nowrap}
.feature-tags{left:146px;top:44px}
.tag--dark{background:var(--grey-dark)}
.feature-copy{left:146px;top:79px;width:222px;font-size:5.9px;line-height:7.9px;color:#6b6c6f}
.slot{position:absolute}
.slot-text{font-size:5.6px;line-height:7px;color:#6b6c6f;margin-top:5px}
.slot--left{left:71px;width:104px}
.slot--left .slot-text{margin-left:13px;width:92px}
.slot--right{left:178px;width:122px}
.slot--right .slot-text{margin-left:22px;width:96px}
.tag--lime{background:var(--lime)}
.tag--cyan{background:var(--cyan)}
.tag--orange{background:var(--orange)}
.tag--plum{background:var(--magenta)}
.slot-photo{position:absolute;width:53px;height:60px;border-radius:9px}
</style>
</head>
<body>
<div class="canvas">

  <!-- Front cover -->
  <section class="page page--cover cover">
    <div class="cover-photo" role="img" aria-label="Photo of a woman dancing with a flowing pink scarf on a sunny beach"></div>
    <svg class="shapes" viewBox="0 0 376 484" aria-hidden="true">
      <path d="M0 0H376V22C345 70 295 102 228 107C150 113 70 104 22 84C10 78 0 70 0 62Z" fill="var(--magenta)" opacity=".95"/>
      <circle cx="59" cy="342" r="77" fill="var(--chartreuse)" opacity=".92"/>
      <circle cx="342" cy="398" r="74" fill="var(--orange)" opacity=".93"/>
      <path d="M0 380C60 370 125 378 190 394C245 410 275 444 288 484H0Z" fill="var(--plum)" opacity=".9"/>
    </svg>
    <div class="abs brand brand-name"><span class="brand-dot"></span>LANTERN GROVE SHOWS</div>
    <div class="abs brand brand-year">EXPO 2013</div>
    <div class="abs event-info">
      <div class="event-city">DENVER</div>
      <div class="event-venue">COPPER EXCHANGE</div>
      <div class="event-dates">SEPT 6-8</div>
      <div class="event-hours">FRI 1-9, SAT 10-7, SUN 10-6</div>
      <div class="event-admission">ADMISSION $5</div>
    </div>
    <div class="abs cover-tagline"><div class="t1">Natural Health</div><div class="t2">Personal Growth</div></div>

    <div class="portrait portrait--round" style="left:92px;top:302px;width:34px;height:34px" role="img" aria-label="Keynote speaker portrait"></div>
    <div class="abs speaker speaker--keynote">
      <h3>Keynote</h3>
      <ul><li>Energy healing talk</li><li>Mindful living hour</li><li>Sound bath session</li></ul>
    </div>

    <div class="portrait portrait--round" style="left:306px;top:322px;width:34px;height:34px" role="img" aria-label="Portrait of Tobin Ashe"></div>
    <div class="abs speaker speaker--right">
      <h3>Tobin<br>Ashe</h3>
      <ul><li>Crystal circle talk</li><li>Aura reading demo</li></ul>
    </div>

    <div class="portrait portrait--round" style="left:56px;top:404px;width:34px;height:34px" role="img" aria-label="Portrait of Mara Lindqvist"></div>
    <div class="abs speaker speaker--bottom">
      <h3>Mara Lindqvist</h3>
      <ul><li>Healing with breath and movement</li></ul>
    </div>

    <div class="abs cover-stats">
      <div class="s1">220 EXHIBITORS</div>
      <div class="s2">80 HEALERS &amp; READERS</div>
      <div class="s3">65 FREE SEMINARS</div>
    </div>
  </section>

  <!-- Welcome page -->
  <section class="page page--welcome welcome">
    <svg class="shapes" viewBox="0 0 376 484" aria-hidden="true">
      <path d="M376 42C320 74 230 86 180 104C148 118 146 200 160 248C174 292 240 292 300 286C340 282 376 296 376 296Z" fill="var(--grey-light)"/>
      <path d="M104 0H376V58C336 52 300 88 250 96C180 106 130 72 114 40C108 26 104 12 104 0Z" fill="var(--lime)"/>
      <path d="M0 262C22 240 62 232 112 236C176 242 208 290 202 352C196 420 166 484 166 484H0Z" fill="var(--plum)"/>
    </svg>
    <div class="abs section-bar toc-title">what's in</div>
    <ul class="abs toc">
      <li><span>Welcome &amp; Directions</span><span>3</span></li>
      <li><span>Ordering Tickets</span><span>5</span></li>
      <li><span>Conference Schedule</span><span>6-8</span></li>
      <li><span>Keynotes</span><span>9-14</span></li>
      <li><span>Workshops</span><span>15-21</span></li>
      <li><span>Exhibitors &amp; Floorplan</span><span>23-25</span></li>
      <li><span>Yoga Dome</span><span>27</span></li>
      <li><span>Panels</span><span>28-29</span></li>
      <li><span>Music Stage</span><span>30</span></li>
      <li><span>Friday Lectures</span><span>32-35</span></li>
      <li><span>Saturday Lectures</span><span>36-43</span></li>
      <li><span>Sunday Lectures</span><span>44-45</span></li>
      <li><span>Longevity Pavilion</span><span>46-47</span></li>
    </ul>
    <h2 class="abs welcome-title">Welcome</h2>
    <div class="abs welcome-greeting">Hi everyone!</div>
    <div class="abs welcome-copy">
      <p>For many of us the name Tall Cedar Expo takes us back to the very emergence of the holistic era. Back in the 80s and 90s the expos crossed the country and served as the home base for the emerging world view that has swept the globe. A great many of the ideas, health practices, and lifestyles practiced in our daily life first appeared at the expos. Along the way we sometimes have forgotten what an amazing community we have built. At Tall Cedar Expo we will celebrate that wonderful vision that we started more than 30 years ago.</p>
      <p>At the expo we have done more than bring some companies together. We have built an exhibit hall of themed villages of booths, with their own stages, colors and designs. We even have a dome for movement and yoga classes in the hall. We have the largest presentation schedule ever assembled, with more than 250 speaking slots filled with the very best presenters both in Chicagoland and across the country. Highlighting the list, the author of the number one book in America, Letters from the Light, Dr Ilan Brookes.</p>
      <p class="welcome-sign">Rowan</p>
    </div>
    <div class="abs brand brand-name"><span class="brand-dot"></span>LANTERN GROVE SHOWS</div>
    <div class="abs brand brand-year">EXPO 2013</div>
    <div class="abs team-note">
      <strong>TEAM MEMBER</strong>
      At the expo we have done more than bring some companies together. We have built an exhibit hall of themed villages of booths, with their own stages, colors and designs. We even have a dome for movement and yoga classes in the hall. We have the largest presentation schedule ever assembled, with more than 250 speaking slots filled with the very best presenters both
    </div>
    <div class="abs section-bar expo-title">expo</div>
    <div class="abs expo-copy">Vero officiis andantur, ut quia nesciligendi cusa quae porem volor simuscia dellupt aturemp oremperis acero que volore lab ipicidoint, officia eperferum eum este dolorerit</div>
    <div class="abs expo-photo" role="img" aria-label="Photo of a busy expo hall crowd"></div>
    <div class="abs expo-copy-side">latamusam faccus denis magnimagnis auta dus, sam as am, comnimi licipsus sundit aut et voluptae expero experore, net quae aliae vo-</div>
    <div class="folio">Lantern Grove Shows Expo 2013 <b>03</b></div>
  </section>

  <!-- Saturday schedule page -->
  <section class="page page--schedule">
    <svg class="shapes" viewBox="0 0 376 484" aria-hidden="true">
      <path d="M100 0H376V118C330 134 250 140 180 135C140 131 110 110 100 80Z" fill="var(--grey-light)"/>
      <path d="M6 0H122C126 44 120 84 96 112C80 130 60 140 40 135C16 128 4 102 4 70Z" fill="var(--grey-dark)"/>
      <path d="M162 10H376V38H132C137 24 146 12 162 10Z" fill="var(--orange)"/>
    </svg>
    <h2 class="abs schedule-title">Saturday Presentation</h2>
    <div class="abs portrait portrait--round feature-portrait" role="img" aria-label="Portrait of featured presenter Owen Marsh"></div>
    <div class="abs feature-tags">
      <span class="tag tag--dark" style="width:93px">Owen Marsh</span>
      <span class="tag tag--dark" style="width:110px">Channeled Healing</span>
      <span class="tag tag--dark" style="width:82px">Meditation</span>
    </div>
    <p class="abs feature-copy">Dr Felix Aldane Foremost Factors in Health and Longevity Dr. Aldane has worked with Raleigh-based Solwell Labs to design a whole food nutritional supplement that incorporates the nutrients and foods consumed in the World's Longevity Hot Spots. He also closely compared the lifestyle choices of people there with the average American lifestyle and designed a wellness protocol called the Pathway for Life, that offers simple suggestions for integrating these lessons into daily life. The Pathway</p>

    <div class="slot-photo portrait" style="left:12px;top:143px" role="img" aria-label="Presenter portrait"></div>
    <div class="slot slot--left" style="top:146px">
      <span class="tag tag--lime" style="width:70px">10 am</span>
      <span class="tag tag--lime" style="width:74px">Channeled Healing</span>
      <span class="tag tag--lime" style="width:52px">Meditation</span>
      <p class="slot-text">Owen Marsh utilizes psychic reading, spiritual channeling, bodywork and metaphysical healing as he guides the individual into a place of aliveness and ease. Join him as he presents a channeled healing meditation assisting those present in their transformational process. Owen travels the United States sharing his healing work.</p>
    </div>
    <div class="slot slot--right" style="top:146px">
      <span class="tag tag--cyan" style="width:122px">12 am</span>
      <span class="tag tag--cyan" style="width:96px">Channeled Healing</span>
      <span class="tag tag--cyan" style="width:62px">Meditation</span>
      <p class="slot-text">Owen Marsh utilizes psychic reading, spiritual channeling, bodywork and metaphysical healing as he guides the individual into a place of aliveness and ease. Join him as he presents a channeled healing meditation assisting those present in their transformational process. Owen travels the United States sharing his healing work.</p>
    </div>
    <div class="slot-photo portrait" style="left:303px;top:143px" role="img" aria-label="Presenter portrait"></div>

    <div class="slot-photo portrait" style="left:12px;top:262px" role="img" aria-label="Presenter portrait"></div>
    <div class="slot slot--left" style="top:265px">
      <span class="tag tag--orange" style="width:70px">11 am</span>
      <span class="tag tag--orange" style="width:74px">Channeled Healing</span>
      <span class="tag tag--orange" style="width:52px">Meditation</span>
      <p class="slot-text">Owen Marsh utilizes psychic reading, spiritual channeling, bodywork and metaphysical healing as he guides the individual into a place of aliveness and ease. Join him for a channeled healing meditation.</p>
    </div>
    <div class="slot slot--right" style="top:265px">
      <span class="tag tag--plum" style="width:122px">13 pm</span>
      <span class="tag tag--plum" style="width:96px">Channeled Healing</span>
      <span class="tag tag--plum" style="width:62px">Meditation</span>
      <p class="slot-text">Owen Marsh utilizes psychic reading, spiritual channeling, bodywork and metaphysical healing as he guides the individual into a place of aliveness and ease. Join him for a channeled healing meditation.</p>
    </div>
    <div class="slot-photo portrait" style="left:303px;top:262px" role="img" aria-label="Presenter portrait"></div>

    <div class="slot-photo portrait" style="left:12px;top:359px" role="img" aria-label="Presenter portrait"></div>
    <div class="slot slot--left" style="top:363px">
      <span class="tag tag--plum" style="width:70px">11.30 am</span>
      <span class="tag tag--plum" style="width:74px">Channeled Healing</span>
      <span class="tag tag--plum" style="width:52px">Meditation</span>
      <p class="slot-text">Owen Marsh utilizes psychic reading, spiritual channeling, bodywork and metaphysical healing as he guides the individual into a place of aliveness and ease. Join him as he presents a channeled healing meditation assisting those present.</p>
    </div>
    <div class="slot slot--right" style="top:363px">
      <span class="tag tag--orange" style="width:122px">17 pm</span>
      <span class="tag tag--orange" style="width:96px">Channeled Healing</span>
      <span class="tag tag--orange" style="width:62px">Meditation</span>
      <p class="slot-text">Owen Marsh utilizes psychic reading, spiritual channeling, bodywork and metaphysical healing as he guides the individual into a place of aliveness and ease. Join him as he presents a channeled healing meditation assisting those present.</p>
    </div>
    <div class="slot-photo portrait" style="left:303px;top:359px" role="img" aria-label="Presenter portrait"></div>

    <div class="folio">Lantern Grove Shows Expo 2013 <b>05</b></div>
  </section>

</div>
</body>
</html>
```